MEDITERRANEAN Cafe Website needed

We are a MEDITERRANEAN Café serving Coffee, breakfast, Pizza, Pasta, Sandwiches etc.

We need a home page, menu & venue, Reservations & Events, Delivery
Connect (Social media / Feedback / Contact us),Join our team
Updates

Can we keep the designs in Mediterranean colours, look, and feel pleasethanks Added Saturday, December 10, 2016

Project Deadline Extended Reason: I have guarantied the payment and upgraded the project. I would like this would to give more time for new designs to come in and a couple of potential designs to show more. Added Sunday, December 11, 2016

Industry/Entity Type

Cafe

Coding

Coded - Design and coding required

Number of Pages Required

5+ page

Requirements
Must have
• MEDITERRANEAN feel, colours, style etc.
• http://www.quillandfen (DOT) co (DOT) uk
Nice to have

```html
<!DOCTYPE html>
<html lang="en">
<head>
<meta charset="utf-8">
<title>Saltera Cafe</title>
<link href="https://fonts.googleapis.com/css2?family=Josefin+Sans:wght@300;400&family=Open+Sans:wght@400;600&display=swap" rel="stylesheet">
<style>
:root{
  --red:#d33b3b;
  --cream:#f6efdc;
  --header:#f7f6f4;
  --ink:#333;
  --muted:#9a948a;
  --white:#fff;
}
*{box-sizing:border-box;margin:0;padding:0}
html,body{width:674px;height:1200px;overflow:hidden}
body{background:var(--cream);font-family:"Open Sans",Arial,sans-serif;color:var(--ink);position:relative}
.abs{position:absolute}
.site-header{left:0;top:0;width:674px;height:50px;background:var(--header)}
.brand{left:74px;top:14px;display:flex;align-items:center;gap:6px}
.brand-dot{width:12px;height:12px;border-radius:50%;background:var(--red)}
.brand-name{font-family:"Josefin Sans",sans-serif;font-size:19px;color:var(--red)}
.main-nav{right:74px;top:19px;display:flex;gap:14px;font-size:7.5px;color:#555}
.main-nav .active{color:var(--red)}
.hero{left:0;top:50px;width:674px;height:295px;background:linear-gradient(120deg,#8f8b86,#b1aca5 50%,#c4beb6)}
.slide-arrow{top:188px;width:14px;height:18px;background:rgba(70,70,70,.55)}
.slide-arrow svg{display:block;margin:5px auto}
h2{font-family:"Josefin Sans",sans-serif;font-weight:300;color:var(--red)}
.welcome-title{left:0;width:674px;top:376px;text-align:center;font-size:18px}
.welcome-text{left:74px;width:526px;top:400px;text-align:center;font-size:6.8px;line-height:11px;color:#555}
.menu-title{left:74px;top:464px;font-size:17px}
.carousel-btn{top:466px;width:13px;height:12px;border:1px solid #999}
.carousel-btn svg{display:block;margin:2px auto}
.menu-item{top:490px;width:124px}
.menu-photo{width:124px;height:90px}
.menu-name{margin-top:5px;text-align:center;color:var(--red);font-size:7.5px;font-weight:400}
.menu-desc{margin-top:2px;text-align:center;font-size:5.3px;line-height:7.5px;color:#333}
.about{left:0;top:638px;width:674px;height:157px;background:linear-gradient(90deg,#4a4540,#6b6258 50%,#4e4843)}
.about-title{left:0;width:674px;top:673px;text-align:center;font-size:17px;color:var(--white)}
.about-text{left:74px;width:526px;top:696px;text-align:center;font-size:6.8px;line-height:11px;color:var(--white)}
.btn-more{left:312px;top:735px;width:50px;height:22px;background:var(--white);font-size:6.8px;text-align:center;line-height:22px;color:#333}
.events-title{left:74px;top:826px;font-size:17px}
.btn-all{left:572px;top:831px;width:28px;height:11px;background:var(--red);color:var(--white);font-size:5px;text-align:center;line-height:11px}
.event{top:855px;width:161px;height:80px;background:var(--white);display:flex}
.event-date{flex:none;width:26px;background:var(--red);color:var(--white);text-align:center;padding-top:8px}
.event-day{font-family:"Josefin Sans",sans-serif;font-size:12px;line-height:12px}
.event-month{font-size:6.5px;margin-top:1px}
.event-body{flex:1;padding:12px 8px 0 10px}
.event-head{font-size:7.2px;line-height:10px;color:#222;font-weight:400}
.event-note{margin-top:5px;font-size:5px;line-height:8px;color:var(--muted)}
.event-note b{color:#222;font-weight:600}
.video{left:74px;top:958px;width:526px;height:180px;background:linear-gradient(90deg,#5a3e2a,#8a5a3c 45%,#6a4630)}
.play{left:325px;top:1035px}
.footer-nav{left:74px;top:1160px;font-size:6.5px;color:#333;display:flex;gap:5px}
.copyright{left:74px;top:1176px;font-size:6.5px;color:#333}
.social{left:493px;top:1166px;display:flex;gap:5px}
.social span{width:14px;height:14px;border-radius:50%;background:var(--red)}
</style>
</head>
<body>
<header class="site-header abs">
  <div class="brand abs"><span class="brand-dot"></span><span class="brand-name">Saltera</span></div>
  <nav class="main-nav abs">
    <span class="active">Home</span><span>Our Story</span><span>About Us</span><span>Events</span><span>Our Menu</span><span>Location</span><span>Careers</span><span>Contact Us</span>
  </nav>
</header>

<div class="hero abs" role="img" aria-label="Top view of a pan of baked eggs in tomato sauce, flatbread, coffee and cutlery on a wooden table"></div>
<div class="slide-arrow abs" style="left:0"><svg width="6" height="8"><polyline points="5,0 1,4 5,8" fill="none" stroke="#fff" stroke-width="1"/></svg></div>
<div class="slide-arrow abs" style="left:660px"><svg width="6" height="8"><polyline points="1,0 5,4 1,8" fill="none" stroke="#fff" stroke-width="1"/></svg></div>

<h2 class="welcome-title abs">Welcome to Saltera Cafe</h2>
<p class="welcome-text abs">One of the centerpieces and the Mediterranean symbol of Saltera Cafe its colors which inspire a carefree ease, and invitation to relax in that particular world of Saltera Cafe. The mixture of captivating marina view and fresh ingredients is played in perfect harmony with the restaurant's atmosphere. Our team has a great sense of pride in everything we do and a passion to ensure you have an incredible experience every time.</p>

<h2 class="menu-title abs">Menu Items</h2>
<div class="carousel-btn abs" style="left:570px"><svg width="5" height="7"><polyline points="4,0 1,3.5 4,7" fill="none" stroke="#777"/></svg></div>
<div class="carousel-btn abs" style="left:587px"><svg width="5" height="7"><polyline points="1,0 4,3.5 1,7" fill="none" stroke="#777"/></svg></div>

<div class="menu-item abs" style="left:74px">
  <div class="menu-photo" role="img" aria-label="Pizza on a tiled table" style="background:linear-gradient(135deg,#b7a58e,#7d5a3c)"></div>
  <p class="menu-name">Donec facilisis sagittis</p>
  <p class="menu-desc">Mauris mollis libero vitae ante pellentesque pulvinar cursus elit</p>
</div>
<div class="menu-item abs" style="left:208px">
  <div class="menu-photo" role="img" aria-label="Burger with fries" style="background:linear-gradient(135deg,#e8e2d8,#c08a4a)"></div>
  <p class="menu-name">Donec facilisis sagittis</p>
  <p class="menu-desc">Mauris mollis libero vitae ante pellentesque pulvinar cursus elit</p>
</div>
<div class="menu-item abs" style="left:342px">
  <div class="menu-photo" role="img" aria-label="Pancake stack with berry jam" style="background:linear-gradient(180deg,#8a1f2a,#e9dccb 60%)"></div>
  <p class="menu-name">Donec facilisis sagittis</p>
  <p class="menu-desc">Mauris mollis libero vitae ante pellentesque pulvinar cursus elit</p>
</div>
<div class="menu-item abs" style="left:476px">
  <div class="menu-photo" role="img" aria-label="Breakfast plate with salmon, eggs and asparagus" style="background:linear-gradient(135deg,#5c6055,#e6e4e0 50%,#d97a5a)"></div>
  <p class="menu-name">Donec facilisis sagittis</p>
  <p class="menu-desc">Mauris mollis libero vitae ante pellentesque pulvinar cursus elit</p>
</div>

<section class="about abs" role="img" aria-label="Table set with Mediterranean dishes"></section>
<h2 class="about-title abs">About us</h2>
<p class="about-text abs">With influences from the Mediterranean, Saltera Café was founded with a great deal of intuition into what makes a dining experience great. Saltera Cafe is a place, where people come to chat, meet up or even work. We set out to offer our guests an experience they wouldn't soon forget and an inventive menu selections all made fresh with quality ingredients and served in a warm and casually comfortable setting.</p>
<div class="btn-more abs">View More</div>

<h2 class="events-title abs">EVENTS</h2>
<div class="btn-all abs">View All</div>

<article class="event abs" style="left:74px">
  <div class="event-date"><div class="event-day">06</div><div class="event-month">SEP</div></div>
  <div class="event-body"><p class="event-head">All of your Saltera Café favorites are available, just right, easily and affordable.</p>
  <p class="event-note">Curabitur posuere tortor eget cursus molestie. Nunc lobortis gravida leo a maximus. In luctus sem in dui porta. <b>More</b></p></div>
</article>
<article class="event abs" style="left:257px">
  <div class="event-date"><div class="event-day">06</div><div class="event-month">SEP</div></div>
  <div class="event-body"><p class="event-head">Turn any large party or event into a Saltera Café celebration.</p>
  <p class="event-note">Curabitur posuere tortor eget cursus molestie. Nunc lobortis gravida leo a maximus. In luctus sem in dui porta. <b>More</b></p></div>
</article>
<article class="event abs" style="left:439px">
  <div class="event-date"><div class="event-day">06</div><div class="event-month">SEP</div></div>
  <div class="event-body"><p class="event-head">We will gladly honor requests to modify orders to suit specific health or dietary needs.</p>
  <p class="event-note">Curabitur posuere tortor eget cursus molestie. Nunc lobortis gravida leo a maximus. In luctus sem in dui porta. <b>More</b></p></div>
</article>

<div class="video abs" role="img" aria-label="Grilled fish with lemon and tomatoes on a wooden table"></div>
<svg class="play abs" width="24" height="24" viewBox="0 0 24 24"><circle cx="12" cy="12" r="12" fill="#fff"/><polygon points="9,7 18,12 9,17" fill="#222"/></svg>

<footer>
  <nav class="footer-nav abs"><span>Home</span>|<span>Our Story</span>|<span>About Us</span>|<span>Events</span>|<span>Our Menu</span>|<span>Location</span>|<span>Careers</span>|<span>Contact Us</span></nav>
  <p class="copyright abs">Copyright © 2016 &nbsp;Company name. &nbsp;All rights reserve.</p>
  <div class="social abs"><span></span><span></span><span></span><span></span><span></span><span></span></div>
</footer>
</body>
</html>
```